Designing HTML Email Creative

Hi There,
The goal of this project is to design an HTML Email Creative.
Target Market: Minority Women 25 - 45. Low Household incomes. Stay at home moms. Middle America
Subject of Email Campaign: Top 5 Reasons To Go Back to College
The goal is to make the users Buy the top 5 reasons to go back to school and then Get Matched to Online & Local Colleges.
Call to action: Get Matched to Online & Local Colleges
You can add two buttons, one above the reasons and one below. The text in the button should be: Get Matched to Online & Local Colleges Now!
Your goal is to make the call to action in the email pop out so that users know very easily where to click to visit our site.
Please find attached the copy that is to be used in the creative.
Also, the information needs to be sourced so you can create very small links in the bottom of the email.
Also, we just need the psd file for this. Does not need to be coded.
Also, you can find some successful email creative attached so you have an idea.
Please note that we have updated the word doc with the correct content.
Women 25 - 50 - Low Household Incomes - Middle America
School

```html
<!DOCTYPE html>
<html lang="en">
<head>
<meta charset="utf-8">
<title>Top Reasons to Go Back to College</title>
<link rel="stylesheet" href="https://fonts.googleapis.com/css2?family=Cinzel:wght@400;600&family=Noto+Serif&family=PT+Sans:wght@700&family=Arimo:wght@400;700&display=swap">
<style>
  :root {
    --page-bg: #ffffff;
    --frame-line: #d9dde3;
    --banner-deep: #0a3fc7;
    --banner-mid: #2f74ea;
    --banner-light: #cfe0f7;
    --title-white: #ffffff;
    --title-gold: #f3b21c;
    --heading-blue: #1443b8;
    --lead-grey: #3d3d3d;
    --reason-red: #e02a10;
    --body-grey: #2e2e2e;
    --cta-top: #ff6a3c;
    --cta-bottom: #d2200a;
    --link-blue: #0b3fc9;
    --note-grey: #444444;
    --band-top: #f6f7f9;
    --band-bottom: #e7eaee;
  }
  * { box-sizing: border-box; margin: 0; padding: 0; }
  html, body { width: 714px; height: 1200px; overflow: hidden; background: var(--page-bg); }
  body { position: relative; font-family: "Arimo", Arial, sans-serif; }

  .email-frame {
    position: absolute; left: 14px; top: 10px; width: 686px; height: 990px;
    border: 1px solid var(--frame-line); border-top: none; background: var(--page-bg);
  }
  .hero-banner {
    position: absolute; left: 0; top: 0; width: 686px; height: 266px; overflow: hidden;
    background:
      radial-gradient(ellipse 420px 200px at 620px 210px, var(--banner-light) 0%, rgba(207,224,247,0) 70%),
      linear-gradient(160deg, var(--banner-deep) 0%, var(--banner-mid) 55%, var(--banner-light) 100%);
  }
  .hero-fade {
    position: absolute; left: 0; bottom: 0; width: 460px; height: 120px;
    background: radial-gradient(ellipse 360px 110px at 180px 120px, #ffffff 30%, rgba(255,255,255,0) 100%);
  }
  .hero-art {
    position: absolute; left: 20px; top: 68px; width: 290px; height: 200px;
    border-radius: 40px 60px 30px 30px;
    background: radial-gradient(ellipse at 55% 35%, #3a3a3a 0%, #1b1b1b 45%, rgba(240,240,240,0.9) 75%, rgba(255,255,255,0) 100%);
  }
  .hero-title { position: absolute; right: 58px; top: 40px; text-align: center; font-family: "Cinzel", "Times New Roman", serif; color: var(--title-white); }
  .hero-title .line-top { font-size: 36px; letter-spacing: 1px; line-height: 40px; }
  .hero-title .line-mid { font-size: 23px; letter-spacing: 2px; line-height: 30px; }
  .hero-title .line-big { font-size: 62px; font-weight: 600; color: var(--title-gold); line-height: 70px; margin-top: 4px; text-shadow: 0 2px 3px rgba(0,0,40,0.35); }

  .intro { position: absolute; left: 37px; top: 298px; width: 600px; }
  .intro h1 { font-family: "Noto Serif", Georgia, serif; font-weight: 400; font-size: 33px; color: var(--heading-blue); line-height: 42px; }
  .intro p { font-family: "Noto Serif", Georgia, serif; font-size: 17px; color: var(--lead-grey); line-height: 25px; margin-top: 4px; }

  .cta-button {
    position: absolute; left: 153px; width: 382px; height: 42px; border-radius: 21px;
    background: linear-gradient(var(--cta-top), var(--cta-bottom));
    box-shadow: 0 3px 5px rgba(0,0,0,0.3);
    color: #fff; font-family: "PT Sans", Arial, sans-serif; font-weight: 700; font-size: 17px;
    display: flex; align-items: center; justify-content: center; text-decoration: none;
  }
  .cta-top { top: 406px; }
  .cta-bottom { top: 870px; }

  .reasons { position: absolute; left: 39px; top: 491px; width: 620px; list-style: none; }
  .reason h2 { font-weight: 400; font-size: 14px; color: var(--reason-red); line-height: 18px; }
  .reason p { font-size: 12px; color: var(--body-grey); line-height: 19px; margin-top: 3px; margin-bottom: 12px; }
  .reason b { font-weight: 700; }

  .explore-band {
    position: absolute; left: 0; top: 945px; width: 686px; height: 45px;
    background: linear-gradient(var(--band-top), var(--band-bottom));
    display: flex; align-items: center; justify-content: center;
    font-size: 14px; color: #333;
  }
  .explore-band a { color: var(--link-blue); font-weight: 700; text-decoration: none; margin: 0 4px; }

  .sources { position: absolute; left: 34px; top: 1023px; width: 640px; font-size: 9px; color: var(--note-grey); line-height: 13px; list-style: none; }
  .sources li { margin-bottom: 8px; }
  .sources a { color: var(--link-blue); text-decoration: none; }
</style>
</head>
<body>
  <div class="email-frame">
    <header class="hero-banner">
      <div class="hero-fade"></div>
      <div class="hero-art" role="img" aria-label="Illustration of a black graduation cap with gold tassel beside a rolled diploma tied with red ribbon"></div>
      <div class="hero-title">
        <div class="line-top">TOP REASONS</div>
        <div class="line-mid">TO GO BACK TO</div>
        <div class="line-big">COLLEGE</div>
      </div>
    </header>

    <section class="intro">
      <h1>Empower Yourself!</h1>
      <p>Empower yourself!&nbsp; Education frees you financially and boosts your self-esteem and self-confidence.</p>
    </section>

    <a class="cta-button cta-top" href="#">Get Matched to Online &amp; Local Colleges Now</a>

    <ol class="reasons">
      <li class="reason">
        <h2>1. Education Pays – Make Double the Money</h2>
        <p>College grads <b>earn nearly twice as much</b> as those with only high school diplomas.&nbsp; Median weekly salary with <b>high school diploma, $652</b>.&nbsp; Median weekly salary with <b>Bachelor’s degree $1,066</b>.</p>
      </li>
      <li class="reason">
        <h2>2.&nbsp; Government Grants – Federal Access Grants</h2>
        <p>College is more affordable than you think.&nbsp; <b>Federal Access Grants of up to $5,550</b> are available to qualifying students.&nbsp; Grants are free money, which does not have to be paid back.&nbsp; Other Federal and state grants are also available, as are low cost government loans and countless scholarships.</p>
      </li>
      <li class="reason">
        <h2>3. Lower Unemployment Rates for College Grads.</h2>
        <p>High school graduates 8.3% unemployed, college graduates 4.5 % unemployed.</p>
      </li>
      <li class="reason">
        <h2>4. Make $1 Million More in Lifetime – Retirement Security</h2>
        <p>On average, those with a <b>bachelor’s degree earn a $1 million</b> more in their lifetime than those with a high school diploma.</p>
      </li>
      <li class="reason">
        <h2>5.&nbsp; Be More Employable</h2>
        <p>Of the 2 million plus job added during the recent U.S. economic recovery, the majorities were for college graduates.</p>
      </li>
    </ol>

    <a class="cta-button cta-bottom" href="#">Get Matched to Online &amp; Local Colleges Now</a>

    <div class="explore-band">You with a college degree—oh the places you will go.&nbsp; <a href="#">Click here</a> to explore the possibilities.</div>
  </div>

  <ul class="sources">
    <li>Education Pays," National Wage Data Office, January 28&nbsp; 2013.&nbsp; Accessed April 21, 2013 &lt;<a href="#">www.wagedataoffice.org/emp/chart_001.htm</a>&gt;</li>
    <li>"Access Grants" Student Aid Center--An Office of the National Learning Office. Accessed April 21, 2013.<br>&lt;<a href="#">http://studentaidcenter.org/types/grants-scholarships/access</a>&gt;</li>
    <li>"Education Pays," National Wage Data Office, January 28&nbsp; 2013.&nbsp; Accessed April 21, 2013 &lt;<a href="#">www.wagedataoffice.org/emp/chart_001.htm</a>&gt;</li>
    <li>National Population Survey, October 2012. Accessed April 20, 2013. &lt;<a href="#">www.popsurvey.org/prod/2012pubs/report11-04.pdf</a>&gt;</li>
    <li>Harlow, Janet. "What is a College Education Worth?" Mind Matters Weekly, August 16 2012.&nbsp; Accessed April 20, 2013.<br>&lt;<a href="#">www.mindmattersweekly.com/blog/clear-thinking/201208/college-education-worth</a>&gt;</li>
  </ul>
</body>
</html>
```